Bridgeway, Lantern, and the Quiet Harbor Loop Research Program Website

Overview: This website will serve a new research program (Bridgeway, Lantern, and the Quiet Harbor Loop) at the Fenmoor University School of Medicine. I want a clean, intuitive design that has a navigation bar, but uses icons/graphic buttons to link to the main pages. In an attached Word document, I have provided a basic information architecture for the site, understanding that this project would just generate graphics and code for the 3 pages. I highlighted the 3 pages I'd like designed.
Target market: People who want to participate in our research, or contribute grant funding to specific projects.
Number of page: The design project focuses on 3 pages, but the site must accommodate 6 pages with top-level links. See attached Word doc.
Logo and website header: Please integrate our logo in the header. I've uploaded it as a png file--both with the name of the website and with just the logo image. I imaging the logo would look great in a banner set against an image of a mountain. The two main design themes I want to see included are nature and healthcare.
Text content: I have not yet provided text. Use some dummy text.
Technical Specifications:
- Build using WordPress. We will host this site ourselves on Brimloft using WordPress.
- The design package must be coded.
- The template must be responsive to different platforms (e.g., computer, mobile phone, iPad).
Thank you! I look forward to seeing your designs.
- Ned

```html
<!DOCTYPE html>
<html lang="en">
<head>
<meta charset="utf-8">
<title>Bridgeway, Lantern, and the Quiet Harbor Loop – The Research Program</title>
<link rel="stylesheet" href="https://fonts.googleapis.com/css2?family=Open+Sans:wght@300;400;600;700&family=Ubuntu:wght@400;500;700&display=swap">
<style>
:root{
  --blue:#135a94;
  --navy:#0d3b5c;
  --lime:#7aab32;
  --lime-bright:#3dc21c;
  --forest:#2c6a23;
  --ink:#333;
  --white:#fff;
  --field:#f4f4f4;
}
*{box-sizing:border-box;margin:0;padding:0}
html,body{width:1200px;height:3769px;overflow:hidden}
body{position:relative;background:var(--white);font-family:"Open Sans",sans-serif;color:var(--ink)}
a{color:inherit;text-decoration:none}

/* header */
.site-header{position:absolute;left:0;top:0;width:1200px;height:81px;background:var(--white);z-index:5}
.brand{position:absolute;left:158px;top:20px;display:flex;align-items:center;gap:10px}
.brand-dot{width:38px;height:38px;border-radius:50%;background:var(--lime)}
.brand-name{display:block;font-family:"Ubuntu",sans-serif;font-weight:700;font-size:11px;color:var(--blue);line-height:14px}
.brand-sub{display:block;font-family:"Ubuntu",sans-serif;font-weight:700;font-size:9px;color:var(--lime);line-height:12px}
.main-nav{position:absolute;left:504px;top:31px;display:flex;gap:25px;font-size:14px;color:#333}
.main-nav .active{color:var(--lime)}
.call{position:absolute;left:957px;top:29px;line-height:16px}
.call-label{font-size:12px;color:var(--lime-bright)}
.call-number{font-size:15px;font-weight:700;color:var(--blue)}

/* hero */
.hero-art{position:absolute;left:0;top:81px}
.hero-title{position:absolute;left:158px;top:204px;width:760px;color:var(--white);font-weight:300;font-size:44px;line-height:56px;white-space:nowrap}
.hero-title strong{display:block;font-family:"Ubuntu",sans-serif;font-weight:700;color:var(--lime-bright);font-size:48px;letter-spacing:.5px}
.hero-text{position:absolute;left:158px;top:340px;width:520px;color:var(--white);font-size:18px;font-weight:600;line-height:26px}
.btn{position:absolute;display:flex;align-items:center;justify-content:center;width:115px;height:34px;background:var(--lime);color:var(--white);font-size:12px;font-weight:700;border-radius:16px 0 16px 0;z-index:3}
.btn.light{background:var(--white);color:var(--lime)}
.hero-dots{position:absolute;left:570px;top:543px;display:flex;gap:5px}
.hero-dots span{width:8px;height:8px;border-radius:50%;background:var(--white)}
.hero-dots .on{background:var(--lime)}

/* headings */
.section-title{position:absolute;font-family:"Ubuntu",sans-serif;font-weight:700;font-size:36px;letter-spacing:.5px;z-index:2}
.rule{position:absolute;height:4px;width:76px;background:var(--lime);z-index:2}

/* about */
.about-ring{position:absolute;left:158px;top:686px;width:418px;height:418px;border-radius:50%;border:3px solid var(--lime);background:var(--white);box-shadow:4px 6px 10px rgba(0,0,0,.18);z-index:2}
.about-emblem{position:absolute;left:198px;top:726px;width:338px;height:338px;border-radius:50%;background:radial-gradient(circle,#b7a46a 0%,#6f8a46 45%,#2f5d7e 100%);z-index:3}
.about-text{position:absolute;left:608px;top:803px;width:436px;font-size:12.8px;line-height:21px;color:#333}

/* info */
.info-bg{position:absolute;left:0;top:1080px}
.info-card{position:absolute;top:1430px;width:285px;height:250px;border-radius:14px;background:var(--white);text-align:center}
.info-card.featured{background:var(--lime);color:var(--white)}
.info-card svg{position:absolute;left:50%;transform:translateX(-50%);top:30px}
.info-card h3{position:absolute;top:106px;left:0;width:100%;font-size:17px;font-weight:700;color:var(--navy)}
.info-card.featured h3{color:var(--white)}
.info-card p{position:absolute;top:144px;left:25px;width:235px;font-size:12.5px;line-height:20px;color:#444}
.info-card.featured p{color:#eef6e2}

/* resources */
.resource-card{position:absolute;top:2057px;width:434px;height:268px;border-radius:30px;background:var(--blue);display:flex;align-items:center;justify-content:center;text-align:center;padding:0 58px}
.resource-card a{color:var(--white);font-style:italic;text-decoration:underline;font-size:17px;line-height:23px}

/* contact */
.contact-bg{position:absolute;left:0;top:2590px;width:1200px;height:660px;background:linear-gradient(180deg,#fbf7ef 0%,#f4e2c0 40%,#d79a55 75%,#9c6a3a 100%)}
.contact-panel{position:absolute;left:232px;top:2467px;width:736px;height:463px;border-radius:4px;background:linear-gradient(180deg,#3e6b12 0%,#24603a 45%,#0b3a56 100%)}
.field{position:absolute;background:var(--white);border:1px solid #ccc;font-size:14px;color:#555;padding:10px 13px}
.field.alt{background:var(--field)}

/* footer */
.footer-bg{position:absolute;left:0;top:3140px}
.footer-mark{position:absolute;left:160px;top:3340px;width:80px;height:80px;border-radius:50%;background:rgba(255,255,255,.9)}
.footer-name{position:absolute;left:157px;top:3468px;color:var(--white);font-family:"Ubuntu",sans-serif;font-weight:700;font-size:15px;line-height:18px}
.footer-name span{font-size:13px}
.footer-about{position:absolute;left:157px;top:3522px;width:340px;color:#e9f0ea;font-size:12.3px;line-height:20px}
.footer-head{position:absolute;top:3364px;color:var(--white);font-size:14.5px;letter-spacing:.3px}
.footer-links{position:absolute;left:577px;top:3432px;list-style:none;color:var(--white);font-size:13.5px;line-height:27px}
.newsletter{position:absolute;left:758px;top:3436px;width:284px;height:52px;background:var(--white);display:flex;align-items:center;padding-left:17px;font-size:13px;color:#333}
.newsletter svg{position:absolute;right:24px;top:18px}
.social{position:absolute;left:758px;top:3524px;display:flex;gap:22px}
.social span{width:12px;height:12px;border-radius:50%;background:var(--white)}
.footer-rule{position:absolute;left:158px;top:3643px;width:884px;height:1px;background:rgba(255,255,255,.5)}
.copyright{position:absolute;left:158px;top:3672px;color:var(--white);font-size:13px}
.copyright span{color:var(--lime)}
.legal{position:absolute;right:158px;top:3672px;color:var(--white);font-size:13px;word-spacing:2px}
</style>
</head>
<body>

<header class="site-header">
  <a class="brand" href="#">
    <span class="brand-dot"></span>
    <span>
      <span class="brand-name">Bridgeway, Lantern, and the Quiet Harbor Loop</span>
      <span class="brand-sub">The Research Program</span>
    </span>
  </a>
  <nav class="main-nav">
    <a class="active" href="#">Home</a><a href="#">People</a><a href="#">Projects</a><a href="#">FAQs</a><a href="#">Resources</a><a href="#">Contact</a>
  </nav>
  <div class="call"><div class="call-label">Call Us Today</div><div class="call-number">555-014-2270</div></div>
</header>

<svg class="hero-art" width="1200" height="580" viewBox="0 0 1200 580">
  <defs>
    <linearGradient id="heroSky" x1="0" y1="0" x2="0" y2="1">
      <stop offset="0" stop-color="#2a6d9a"/><stop offset=".6" stop-color="#175683"/><stop offset="1" stop-color="#0e3f66"/>
    </linearGradient>
  </defs>
  <rect width="1200" height="580" fill="url(#heroSky)" role="img" aria-label="Photo of a person standing on a rock facing misty blue mountains"/>
  <path d="M0 470 C120 440 260 450 420 490 C620 540 800 560 940 520 C1040 490 1130 450 1200 420 L1200 580 L0 580 Z" fill="var(--lime)"/>
  <path d="M0 500 C140 480 300 500 480 540 C660 575 820 570 920 540 C1030 505 1130 480 1200 480 L1200 580 L0 580 Z" fill="#fff"/>
</svg>
<h1 class="hero-title">BRIDGEWAY, LANTERN &amp;<strong>THE QUIET HARBOR LOOP</strong></h1>
<p class="hero-text">Lorem Ipsum has been the industry's standard dummy text ever since the 1500s,</p>
<a class="btn" href="#" style="left:158px;top:416px">Learn More</a>
<div class="hero-dots"><span></span><span></span><span class="on"></span><span></span><span></span></div>

<div class="about-ring"></div>
<div class="about-emblem" role="img" aria-label="Program emblem filled with a sunlit meadow photo"></div>
<h2 class="section-title" style="left:608px;top:718px;color:var(--blue)">ABOUT <span style="color:var(--lime)">US</span></h2>
<div class="rule" style="left:608px;top:770px"></div>
<p class="about-text">There are many variations of passages of Lorem Ipsum available, but the majority have suffered alteration in some form, by injected humour, or randomised words which don't look even slightly believable. If you are going to use a passage of Lorem Ipsum, you need to be sure there isn't anything embarrassing hidden in the middle of text. All the Lorem Ipsum generators on the Internet tend to repeat predefined chunks as necessary, making this the first true generator on the Internet.<br>It uses a dictionary of over 200 Latin words, combined with a handful of model sentence structures, to generate Lorem Ipsum which looks reasonable. The generated Lorem Ipsum is therefore always free from repetition, injected humour, or non-characteristic words etc.</p>

<svg class="info-bg" width="1200" height="810" viewBox="0 0 1200 810">
  <defs>
    <linearGradient id="infoFill" x1="0" y1="0" x2="0" y2="1">
      <stop offset="0" stop-color="#2f6c1e"/><stop offset=".45" stop-color="#1f6032"/><stop offset="1" stop-color="#0b3a58"/>
    </linearGradient>
  </defs>
  <rect width="1200" height="810" fill="url(#infoFill)"/>
  <path d="M0 0 L1200 0 L1200 20 C1080 20 960 40 820 70 C640 110 420 120 260 100 C160 85 70 95 0 100 Z" fill="#fff"/>
  <path d="M0 100 C70 95 160 85 260 100 C420 120 640 110 820 70 C960 40 1080 20 1200 20 L1200 60 C1080 55 960 70 820 95 C620 130 420 140 260 122 C150 110 70 108 0 112 Z" fill="var(--lime)"/>
  <path d="M0 680 C140 650 300 660 480 700 C650 735 820 750 940 705 C1040 670 1130 630 1200 610 L1200 810 L0 810 Z" fill="var(--lime)"/>
  <path d="M0 700 C150 680 310 695 480 730 C660 765 820 768 930 730 C1040 695 1130 685 1200 690 L1200 810 L0 810 Z" fill="#fff"/>
</svg>
<h2 class="section-title" style="left:0;width:1200px;text-align:center;top:1314px;color:var(--white)">OUR INFORMATION</h2>
<div class="rule" style="left:562px;top:1365px;background:var(--white)"></div>

<div class="info-card" style="left:158px">
  <svg width="86" height="56" viewBox="0 0 86 56" fill="none" stroke="var(--blue)" stroke-width="2.5"><circle cx="43" cy="12" r="9"/><circle cx="16" cy="16" r="7"/><circle cx="70" cy="16" r="7"/><path d="M26 52 v-8 a17 17 0 0 1 34 0 v8 z"/><path d="M3 50 v-6 a13 13 0 0 1 22 -9"/><path d="M83 50 v-6 a13 13 0 0 0 -22 -9"/></svg>
  <h3>PEOPLE</h3>
  <p>There are many variations of passages of Lorem Ipsum available, but the majority have suffered alteration .</p>
</div>
<a class="btn" href="#" style="left:243px;top:1665px">Learn More</a>

<div class="info-card featured" style="left:458px">
  <svg width="62" height="60" viewBox="0 0 62 60" fill="none" stroke="#fff" stroke-width="2.5"><rect x="4" y="4" width="30" height="52"/><path d="M10 48 v-14 M18 48 v-20 M26 48 v-10"/><circle cx="40" cy="20" r="13" fill="var(--lime)"/><path d="M49 30 l10 10"/></svg>
  <h3>RESEARCH PROJECTS</h3>
  <p>There are many variations of passages of Lorem Ipsum available, but the majority have suffered alteration .</p>
</div>
<a class="btn light" href="#" style="left:543px;top:1665px">Learn More</a>

<div class="info-card" style="left:758px">
  <svg width="58" height="58" viewBox="0 0 58 58" fill="none" stroke="var(--blue)" stroke-width="2.5"><path d="M29 4 a25 25 0 1 1 -14 46 l-10 5 l4 -11 A25 25 0 0 1 29 4 z"/><path d="M22 22 a7 7 0 1 1 10 6 c-3 2 -3 4 -3 7"/><circle cx="29" cy="42" r="1.5" fill="var(--blue)"/></svg>
  <h3>FAQS</h3>
  <p>There are many variations of passages of Lorem Ipsum available, but the majority have suffered alteration .</p>
</div>
<a class="btn" href="#" style="left:843px;top:1665px">Learn More</a>

<h2 class="section-title" style="left:0;width:1200px;text-align:center;top:1970px;color:var(--blue)">RESOURCES</h2>
<div class="rule" style="left:548px;top:2020px"></div>
<div class="resource-card" style="left:158px"><a href="#">There are many variations of passages of Lorem Ipsum available, but the majority have suffered alteration in some form, by injected</a></div>
<div class="resource-card" style="left:608px"><a href="#">There are many variations of passages of Lorem Ipsum available, but the majority have suffered alteration in some form, by injected</a></div>
<a class="btn" href="#" style="left:543px;top:2354px">Learn More</a>

<div class="contact-bg" role="img" aria-label="Photo of a family running through a golden meadow at sunset"></div>
<div class="contact-panel"></div>
<h2 class="section-title" style="left:0;width:1200px;text-align:center;top:2548px;color:var(--white)">CONTACT US</h2>
<div class="rule" style="left:543px;top:2598px;background:var(--white)"></div>
<div class="field" style="left:326px;top:2620px;width:268px;height:41px">First Name *</div>
<div class="field" style="left:604px;top:2620px;width:269px;height:41px">Last Name *</div>
<div class="field" style="left:326px;top:2676px;width:268px;height:41px">Email *</div>
<div class="field alt" style="left:604px;top:2676px;width:269px;height:41px">Ph No *</div>
<div class="field" style="left:326px;top:2730px;width:547px;height:90px">Message</div>
<a class="btn" href="#" style="left:543px;top:2838px">Submit Now</a>

<svg class="footer-bg" width="1200" height="629" viewBox="0 0 1200 629">
  <defs>
    <linearGradient id="footFill" x1="0" y1="0" x2="0" y2="1">
      <stop offset="0" stop-color="#2f6c1e"/><stop offset=".5" stop-color="#1f5a3a"/><stop offset="1" stop-color="#0c3a5a"/>
    </linearGradient>
  </defs>
  <path d="M0 110 C150 60 330 30 520 30 C720 30 900 60 1040 80 C1110 90 1160 95 1200 95 L1200 629 L0 629 Z" fill="url(#footFill)"/>
  <path d="M0 95 C150 50 330 15 520 15 C720 15 900 45 1040 62 C1110 70 1160 72 1200 70 L1200 95 C1160 95 1110 90 1040 80 C900 60 720 30 520 30 C330 30 150 60 0 110 Z" fill="var(--lime)"/>
</svg>
<div class="footer-mark"></div>
<div class="footer-name">Bridgeway, Lantern, and the Quiet Harbor Loop<br><span>The Research Program</span></div>
<p class="footer-about">There are many variations of passages of Lorem Ipsum available, but the majority have suffered alteration in some form, by injected humour, or randomised words which don't look even slightly believable.</p>
<div class="footer-head" style="left:577px">QUICK LINK</div>
<div class="rule" style="left:577px;top:3390px;width:36px;height:3px"></div>
<ul class="footer-links"><li>Home</li><li>People</li><li>Projects</li><li>FAQs</li><li>Resources</li><li>Contact</li></ul>
<div class="footer-head" style="left:758px">SUBSCRIBE NEWSLETTER</div>
<div class="rule" style="left:758px;top:3390px;width:36px;height:3px"></div>
<div class="newsletter">Enter The Mail iD
  <svg width="18" height="16" viewBox="0 0 18 16"><path d="M0 7 L18 0 L13 16 L8 10 Z" fill="var(--lime)"/></svg>
</div>
<div class="social"><span></span><span></span><span></span><span></span></div>
<div class="footer-rule"></div>
<div class="copyright">© 2021 <span>Harborline</span>. All rights reserved.</div>
<div class="legal">Privacy Policy &nbsp;I&nbsp; Terms &amp; Conditions</div>

</body>
</html>
```